Spirit Distillery needs website design for velmorastills.com

We are a spirit distillery located in Canberra, Australia. We are just about to begin production on our products: Gin, Coffee vodka, lemon myrtle vodka, and apple and cinnamon vodka.
Velmora is Ancient Greek Mythology meaning "elixir of the Gods" so Greek mythology incorporated in the website, as well as simple and user friendly layout and functionality would be great.
Pages would include:
Welcome page with links to:
Our Products (Gin, Coffee vodka, lemon myrtle vodka, and apple and cinnamon vodka)
Events (what events the distillery is attending or holding at the distillery site)
Shop (for bottle sales)
Stockists (where the bottles are sold)
Cocktail recipe page

```html
<!DOCTYPE html>
<html lang="en">
<head>
<meta charset="utf-8">
<title>Velmora – velmorastills.com</title>
<link href="https://fonts.googleapis.com/css2?family=Libre+Baskerville:wght@700&family=Roboto:wght@400;500;700&display=swap" rel="stylesheet">
<style>
:root{
  --gold:#c29b4c;
  --gold-light:#e9d6a6;
  --brown:#9a7640;
  --cream:#faf3e6;
  --mustard:#e5c55d;
  --ink:#222222;
  --muted:#8a8a8a;
  --footer:#232323;
  --white:#ffffff;
  --line:#d9d9d9;
}
*{margin:0;padding:0;box-sizing:border-box}
html,body{width:1200px;height:3776px;overflow:hidden;background:var(--white);font-family:"Roboto",sans-serif;color:var(--ink)}
.page{position:relative;width:1200px;height:3776px}
.abs{position:absolute}
.serif{font-family:"Libre Baskerville",serif;font-weight:700}
.section-title{position:absolute;left:0;width:1200px;text-align:center;font-size:50px;color:var(--gold);letter-spacing:1px}
.btn{position:absolute;display:flex;align-items:center;justify-content:center;background:var(--brown);color:var(--white);font-weight:700;font-size:17px;border-radius:32px;text-transform:uppercase}
.arrow{position:absolute;width:44px;height:44px;border-radius:50%;border:1.5px solid #777;background:var(--white);display:flex;align-items:center;justify-content:center}
.photo{position:absolute}

/* header */
.border-band{position:absolute;top:40px;height:46px;background:var(--gold-light)}
.logo{position:absolute;top:28px;left:0;width:1200px;text-align:center;font-size:64px;color:var(--gold);letter-spacing:4px}
.nav{position:absolute;top:134px;left:173px;display:flex;gap:48px;font-size:16px}
.nav span{padding-bottom:8px}
.nav .active{border-bottom:3px solid var(--brown)}
.header-line{position:absolute;top:184px;left:0;width:1200px;height:1px;background:#e3e3e3}

/* hero */
.hero{position:absolute;top:185px;left:0;width:1200px;height:496px;background:linear-gradient(180deg,#3a2a1a 0%,#6b4a28 40%,#4a3622 70%,#8a7a70 100%)}
.hero-title{position:absolute;left:145px;top:300px;font-size:66px;line-height:84px;color:var(--white)}

/* products */
.card{position:absolute;top:898px;width:291px;height:330px;border:1px solid var(--line);border-radius:6px;background:var(--white);overflow:hidden}
.bottle{position:absolute;left:96px;top:14px;width:100px;height:300px;border-radius:30px 30px 16px 16px}
.product-name{position:absolute;width:291px;text-align:center;top:1262px;font-size:20px;font-weight:700}
.price{position:absolute;width:291px;text-align:center;top:1298px;font-size:16px;color:var(--gold)}

/* events */
.events{position:absolute;top:1503px;left:0;width:1200px;height:753px;background:var(--cream)}
.event-card{position:absolute;top:1919px;width:390px;height:233px;background:var(--white);padding:26px 42px}
.event-date{color:var(--gold);font-size:17px;font-weight:500}
.event-head{margin-top:14px;font-size:14.5px;font-weight:700;line-height:26px}
.event-body{margin-top:14px;font-size:12px;line-height:24px;color:var(--muted)}

/* stockists */
.stock-box{position:absolute;left:457px;top:2341px;width:598px;height:457px;background:var(--mustard);padding:56px 66px}
.stock-title{font-size:50px;color:var(--white)}
.stock-body{margin-top:22px;font-size:11.5px;line-height:24px;color:var(--white)}

/* recipe */
.recipe-text{position:absolute;left:230px;top:3100px;width:740px;text-align:center;font-size:13px;line-height:25px;color:var(--muted)}

/* footer */
.footer{position:absolute;top:3479px;left:0;width:1200px;height:297px;background:var(--footer);color:var(--white)}
.social{position:absolute;top:46px;left:543px;display:flex;gap:16px}
.social span{width:30px;height:30px;border-radius:50%;background:var(--white)}
.foot-nav{position:absolute;top:114px;left:0;width:1200px;display:flex;justify-content:center;gap:48px;font-size:15px}
.copy{position:absolute;top:168px;left:0;width:1200px;text-align:center;font-size:12px}
.pay{position:absolute;top:222px;left:476px;display:flex;gap:10px}
.pay span{width:42px;height:28px;border-radius:3px;background:#d9d9d9}
</style>
</head>
<body>
<div class="page">

  <!-- header -->
  <div class="border-band" style="left:0;width:374px" role="img" aria-label="Decorative border ornament"></div>
  <div class="border-band" style="left:826px;width:374px" role="img" aria-label="Decorative border ornament"></div>
  <div class="logo serif">VELMORA</div>
  <nav class="nav">
    <span class="active">HOME</span><span>PRODUCTS</span><span>EVENTS</span><span>SHOP</span><span>STOCKISTS</span><span>COCKTAIL RECIPE</span>
  </nav>
  <svg class="abs" style="left:940px;top:134px" width="82" height="24" viewBox="0 0 82 24">
    <circle cx="9" cy="10" r="6" fill="none" stroke="#c29b4c" stroke-width="2.5"/><line x1="13" y1="14" x2="18" y2="19" stroke="#c29b4c" stroke-width="3"/>
    <path d="M36 10h16l-2 10h-12z" fill="#c29b4c"/><path d="M40 10l4-6 4 6" fill="none" stroke="#c29b4c" stroke-width="2"/>
    <circle cx="58" cy="4" r="5" fill="#111"/><text x="58" y="7" font-size="7" fill="#fff" text-anchor="middle" font-family="Roboto,sans-serif">0</text>
    <circle cx="72" cy="7" r="4" fill="#c29b4c"/><path d="M64 20a8 6 0 0 1 16 0z" fill="#c29b4c"/>
  </svg>
  <div class="header-line"></div>

  <!-- hero -->
  <div class="hero" role="img" aria-label="Three garnished gin cocktails in balloon glasses on a bar counter"></div>
  <div class="hero-title serif">NECTAR OF<br>THE GODS</div>
  <div class="btn" style="left:145px;top:493px;width:200px;height:62px">Shop Products</div>
  <div class="arrow" style="left:556px;top:662px;width:42px;height:42px;border:none"><svg width="12" height="16"><path d="M9 2L3 8l6 6" fill="none" stroke="#222" stroke-width="2"/></svg></div>
  <div class="arrow" style="left:598px;top:662px;width:42px;height:42px;border:none"><svg width="12" height="16"><path d="M3 2l6 6-6 6" fill="none" stroke="#222" stroke-width="2"/></svg></div>

  <!-- products -->
  <div class="section-title serif" style="top:785px">OUR PRODUCTS</div>
  <div class="arrow" style="left:76px;top:1040px"><svg width="12" height="18"><path d="M9 2L3 9l6 7" fill="none" stroke="#444" stroke-width="2"/></svg></div>
  <div class="arrow" style="left:1080px;top:1040px"><svg width="12" height="18"><path d="M3 2l6 7-6 7" fill="none" stroke="#444" stroke-width="2"/></svg></div>

  <div class="card" style="left:144px"><div class="bottle" role="img" aria-label="Clear gin bottle with bronze label" style="background:linear-gradient(180deg,#eef0f0,#b89a6e 55%,#d9d3c8)"></div></div>
  <div class="card" style="left:454px"><div class="bottle" role="img" aria-label="Pale gold vodka bottle with bronze label" style="background:linear-gradient(180deg,#efe6b8,#b8a066 55%,#e2d7a0)"></div></div>
  <div class="card" style="left:764px"><div class="bottle" role="img" aria-label="Dark brown coffee vodka bottle with bronze label" style="background:linear-gradient(180deg,#8a5a3a,#6a4026 55%,#9a7050)"></div></div>

  <div class="product-name" style="left:144px">PRODUCT NAME</div>
  <div class="product-name" style="left:454px">PRODUCT NAME</div>
  <div class="product-name" style="left:764px">PRODUCT NAME</div>
  <div class="price" style="left:144px">$56.75</div>
  <div class="price" style="left:454px">$56.75</div>
  <div class="price" style="left:764px">$56.75</div>
  <div class="btn" style="left:210px;top:1342px;width:159px;height:62px">Shop Now</div>
  <div class="btn" style="left:520px;top:1342px;width:159px;height:62px">Shop Now</div>
  <div class="btn" style="left:830px;top:1342px;width:159px;height:62px">Shop Now</div>

  <!-- events -->
  <div class="events"></div>
  <div class="section-title serif" style="top:1600px">OUR EVENTS</div>
  <div class="arrow" style="left:76px;top:1856px"><svg width="12" height="18"><path d="M9 2L3 9l6 7" fill="none" stroke="#444" stroke-width="2"/></svg></div>
  <div class="arrow" style="left:1080px;top:1856px"><svg width="12" height="18"><path d="M3 2l6 7-6 7" fill="none" stroke="#444" stroke-width="2"/></svg></div>
  <div class="photo" style="left:144px;top:1721px;width:438px;height:314px;background:linear-gradient(135deg,#2e2420,#8a8680 50%,#3a2e26)" role="img" aria-label="Bartender pouring a garnished cocktail"></div>
  <div class="photo" style="left:618px;top:1721px;width:437px;height:314px;background:linear-gradient(135deg,#6a5040,#d8d2c8 50%,#9a7a60)" role="img" aria-label="Friends toasting with colourful cocktails"></div>
  <div class="event-card" style="left:168px">
    <div class="event-date">Aug 26,2021</div>
    <div class="event-head">LOREM IPSUM DOLOR SIT AMET<br>CONSECTETUR DIPISCING</div>
    <div class="event-body">Lorem ipsum dolor sit amet, consectetur adipiscing elit, sed do eiusmod tempor incididunt ut labore et dolore magna aliqua.is ipsum suspendisse ultriravida.</div>
  </div>
  <div class="event-card" style="left:642px">
    <div class="event-date">Aug 26,2021</div>
    <div class="event-head">LOREM IPSUM DOLOR SIT AMET<br>CONSECTETUR DIPISCING</div>
    <div class="event-body">Lorem ipsum dolor sit amet, consectetur adipiscing elit, sed do eiusmod tempor incididunt ut labore et dolore magna aliqua.is ipsum suspendisse ultriravida.</div>
  </div>

  <!-- stockists -->
  <div class="photo" style="left:0;top:2256px;width:526px;height:627px;background:linear-gradient(160deg,#1e1a18,#4a3a30 50%,#2a2220)" role="img" aria-label="Bartender garnishing a gin and tonic with a lime wheel"></div>
  <div class="stock-box">
    <div class="stock-title serif">STOCKISTS</div>
    <div class="stock-body">Lorem ipsum dolor sit amet, consectetur adipiscing elit, sed do eiusmod tempor incididunt ut labore et dolore magna aliqua. Quis ipsum suspendisse ultrices gravida. Risus commodo viverra maecenas accumsan lacus vel facilisis. Lorem ipsum dolor sit amet, consectetur adipiscing elit, sed do eiusmod tempor incididunt ut labore et dolore magna aliqua. Quis ipsum suspendisse ultrices gravida. Risus commodo viverra maecenas accumsan lacus vel facilisis.</div>
  </div>
  <div class="btn" style="left:525px;top:2669px;width:160px;height:62px">Read More</div>

  <!-- cocktail recipe -->
  <div class="photo" style="left:30px;top:3164px;width:1140px;height:250px;background:radial-gradient(ellipse at center,#f4f4f4 0%,#ebebeb 60%,#ffffff 100%);opacity:.8" role="img" aria-label="Faint top-down pattern of cocktail glasses"></div>
  <div class="section-title serif" style="top:2998px">COCKTAIL RECIPE</div>
  <div class="recipe-text">Lorem ipsum dolor sit amet, consectetur adipiscing elit, sed do eiusmod tempor incididunt ut labore et dolore magna aliqua. Quis ipsum suspendisse ultrices gravida. Risus commodo viverra maecenas accumsan lacus vel facilisis. Lorem ipsum dolor sit amet, consectetur adipiscing elit, sed do eiusmod tempor incididunt ut labore et dolore magna aliqua. Quis ipsum suspendisse ultrices gravida. Risus commodo viverra maecenas accumsan lacus vel facilisis. Lorem ipsum dolor sit amet, consectetur adipiscing elit, sed do eiusmod tempor incididunt ut labore et dolore magna aliqua. Quis ipsum suspendisse ultrices gravida. Risus commodo viverra maecenas accumsan lacus vel facilisis.</div>
  <div class="btn" style="left:521px;top:3277px;width:159px;height:62px">Read More</div>

  <!-- footer -->
  <footer class="footer">
    <div class="social"><span></span><span></span><span></span></div>
    <div class="foot-nav"><span>HOME</span><span>PRODUCTS</span><span>EVENTS</span><span>SHOP</span><span>STOCKISTS</span><span>COCKTAIL RECIPE</span></div>
    <div class="copy">© 2021 Velmora. All rights reserved &nbsp;|&nbsp; Privacy &nbsp;|&nbsp; Terms of Use</div>
    <div class="pay"><span></span><span></span><span></span><span></span><span></span></div>
  </footer>
</div>
</body>
</html>
```